Private Optometric Practice Needs new Presentation Folders/Stationary

We recently moved our office and are looking to refresh our presentation folders and stationary. I tend to prefer simple, clean designs. We are a full scope optometric practice provide high quality eyewear, custom contact lenses, along with emergency care and treatment for dry eyes. We communicate with a lot of other doctors and want to exude professionalism. I have attached 2 versions of our logo.

Target Market(s)

Familys

Industry/Entity Type

Eyecare

Font styles to use
Sans Serif

Colors
0054AA
0677BA
7BADD7
CADEEF
E8F1F8

Requirements
Nice to have
• Bifold, areas to put information about practice, welcome letter

```html
<!DOCTYPE html>
<html lang="en">
<head>
<meta charset="utf-8">
<title>Clearview Eyecare – Business Card</title>
<link rel="stylesheet" href="https://fonts.googleapis.com/css2?family=Montserrat:wght@400;500;600&display=swap">
<style>
  :root {
    --page-bg: #e0e0e0;
    --panel-navy: #061722;
    --panel-blue: #38a8df;
    --brand-blue: #38a8df;
    --text-white: #ffffff;
  }
  * { margin: 0; padding: 0; box-sizing: border-box; }
  html, body {
    width: 1200px;
    height: 1200px;
    overflow: hidden;
    background: var(--page-bg);
    font-family: "Montserrat", sans-serif;
  }
  .business-card {
    position: absolute;
    left: 78px;
    top: 294px;
    width: 1044px;
    height: 611px;
    display: flex;
  }
  .brand-panel {
    width: 442px;
    height: 100%;
    background: var(--panel-navy);
    display: flex;
    flex-direction: column;
    align-items: center;
    justify-content: center;
    gap: 22px;
  }
  .brand-mark {
    width: 62px;
    height: 62px;
    border-radius: 50%;
    background: var(--brand-blue);
  }
  .brand-name {
    color: var(--text-white);
    font-weight: 400;
    font-size: 34px;
    letter-spacing: 0.22em;
    text-align: center;
    line-height: 1.25;
    padding-left: 0.22em;
  }
  .contact-panel {
    flex: 1;
    height: 100%;
    background: var(--panel-blue);
    color: var(--text-white);
    position: relative;
  }
  .doctor-name {
    position: absolute;
    left: 75px;
    top: 159px;
    font-weight: 600;
    font-size: 27px;
    letter-spacing: 0.03em;
  }
  .office-address {
    position: absolute;
    left: 75px;
    top: 247px;
    font-style: normal;
    font-weight: 400;
    font-size: 22px;
    line-height: 29px;
  }
  .contact-list {
    position: absolute;
    left: 72px;
    top: 389px;
    list-style: none;
    font-size: 20px;
    font-weight: 400;
  }
  .contact-item {
    display: flex;
    align-items: center;
    gap: 18px;
    height: 32px;
  }
  .contact-icon {
    width: 20px;
    height: 20px;
    flex: none;
  }
</style>
</head>
<body>
  <div class="business-card">
    <section class="brand-panel">
      <div class="brand-mark"></div>
      <div class="brand-name">CLEARVIEW<br>EYECARE</div>
    </section>
    <section class="contact-panel">
      <h1 class="doctor-name">DANIEL WHITCOMBE, O.D.</h1>
      <address class="office-address">
        4120 HARBOR POINTE DR.<br>
        SUITE B<br>
        RIDGEVIEW, MI 48201
      </address>
      <ul class="contact-list">
        <li class="contact-item">
          <svg class="contact-icon" viewBox="0 0 24 24" aria-hidden="true">
            <path fill="#fff" d="M6.6 2.5c.6-.4 1.4-.2 1.8.4l2 3.2c.3.6.2 1.3-.3 1.7l-1.5 1.2c.9 2.2 2.3 4 4.3 5.5l1.4-1.3c.5-.4 1.2-.5 1.7-.1l3.1 2.1c.6.4.8 1.2.4 1.8l-1.1 1.9c-.6 1-1.8 1.5-3 1.1C9.6 18.3 5.6 13.8 4.4 7.4c-.2-1.1.3-2.2 1.2-2.9z"/>
          </svg>
          <span>248-555-0172</span>
        </li>
        <li class="contact-item">
          <svg class="contact-icon" viewBox="0 0 24 24" aria-hidden="true" fill="none" stroke="#fff" stroke-width="1.6">
            <circle cx="12" cy="12" r="9"/>
            <ellipse cx="12" cy="12" rx="4" ry="9"/>
            <line x1="3" y1="12" x2="21" y2="12"/>
            <path d="M5 7.5h14M5 16.5h14"/>
          </svg>
          <span>WWW.CLEARVIEWEYECARECENTER.COM</span>
        </li>
      </ul>
    </section>
  </div>
</body>
</html>
```